Market online tutoring + Back to School + give Support for students school work K to 12 Grade

To promote my tutoring business online need to create a two sided flyer. Need to get the attention of parents and educators who looking for help to support the digital learning of their students due to COVID-19 lock down. I need to project and differentiate that we offer support for online school with individualized learning . We tutor Elementary to High school students on all subjects you may take a look at my website qnacademyga.com for additional info and also I can provide
Updates

Hi All Due to Covid, we were unable to work on this project on time as originally planned. We were given an extension until March 15 and we will complete it by then. Sorry for any inconvenience and Thank you for your support. -QN Academy

Target Market(s)

Parents and students

Industry/Entity Type

Education

Requirements
Must have
• For online less fine print on the first page. The phone number and support text message. Back to School , Support Online learning KEV/NUR test prep should have some focus
Nice to have
• Discuss the platform We created a platform with live instructor interaction, virtual classroom, instructional videos, assessments, and practice to support every individual student’s need. We are confident in our ability to provide the most effective distance learning experience.
Should not have
• too much clunky and packed with content. Should be easy to read with color

```html
<!DOCTYPE html>
<html lang="en">
<head>
<meta charset="utf-8">
<title>QN Academy – Back to School Flyer</title>
<link rel="stylesheet" href="https://fonts.googleapis.com/css2?family=Alfa+Slab+One&family=Montserrat:wght@400;500;600;700&display=swap">
<style>
  :root {
    --stage: #2c2c2c;
    --navy: #0f3340;
    --yellow: #dcbd2e;
    --red: #b8142b;
    --white: #ffffff;
    --photo-warm: #b48a4a;
    --photo-dark: #4a3a2c;
    --photo-soft: #e3cdbf;
    --board: #3c4a44;
  }
  * { margin: 0; padding: 0; box-sizing: border-box; }
  html, body { width: 1200px; height: 900px; overflow: hidden; }
  body {
    background: var(--stage);
    font-family: "Montserrat", Arial, sans-serif;
    position: relative;
  }
  .flyer { position: absolute; background: var(--white); overflow: hidden; }
  .flyer-front { left: 68px; top: 40px; width: 520px; height: 672px; }
  .flyer-back { left: 640px; top: 180px; width: 517px; height: 670px; }
  .shapes { position: absolute; inset: 0; width: 100%; height: 100%; }
  .abs { position: absolute; }

  /* Front */
  .headline {
    left: 27px; top: 40px;
    font-family: "Alfa Slab One", Georgia, serif;
    color: var(--white);
    font-size: 52px; line-height: 1.0; letter-spacing: 4px;
  }
  .headline-rule { left: 27px; top: 211px; width: 267px; height: 3px; background: var(--white); }
  .subhead {
    left: 28px; top: 227px;
    color: var(--navy); font-size: 24px; font-weight: 600; line-height: 1.25;
  }
  .brand {
    left: 378px; top: 88px; display: flex; align-items: center; gap: 7px;
    color: var(--navy); font-weight: 700; font-size: 15px; white-space: nowrap;
  }
  .brand-dot { width: 14px; height: 14px; border-radius: 50%; background: var(--red); }
  .photo { border-radius: 50%; }
  .front-photo {
    left: 206px; top: 208px; width: 318px; height: 366px;
    background: radial-gradient(circle at 45% 45%, var(--photo-warm), var(--photo-dark));
  }
  .section-title { left: 33px; top: 382px; color: var(--navy); font-size: 20px; font-weight: 700; }
  .about-text {
    left: 33px; top: 420px; width: 172px;
    color: var(--navy); font-size: 9.2px; line-height: 1.27;
  }
  .about-text p + p { margin-top: 9px; }
  .test-tags { left: 33px; top: 601px; display: flex; }
  .tag {
    width: 77px; height: 24px; color: var(--white);
    font-size: 17px; font-weight: 700; display: flex; align-items: center; justify-content: center;
  }
  .tag-navy { background: var(--navy); }
  .tag-red { background: var(--red); }
  .tags-caption {
    left: 33px; top: 628px; width: 154px; text-align: center;
    color: var(--navy); font-size: 7.5px; font-weight: 700; letter-spacing: .3px;
  }
  .front-contact { left: 316px; top: 590px; width: 150px; text-align: center; }
  .contact-label { color: var(--white); font-size: 17px; font-weight: 600; }
  .phone-pill {
    display: inline-block; margin-top: 3px; padding: 2px 17px;
    background: var(--red); color: var(--white); border-radius: 12px;
    font-size: 16px; font-weight: 500; white-space: nowrap;
  }

  /* Back */
  .back-title { left: 28px; top: 38px; color: var(--yellow); font-size: 22px; font-weight: 700; }
  .back-text { left: 27px; top: 80px; color: var(--white); font-size: 9.2px; line-height: 1.22; }
  .back-text p { margin-bottom: 10px; }
  .back-text .p-wide { width: 318px; }
  .back-text .p-mid { width: 292px; }
  .back-text .p-narrow { width: 226px; }
  .back-photo-1 {
    left: 332px; top: 117px; width: 180px; height: 180px;
    background: radial-gradient(circle at 50% 45%, var(--photo-soft), #a2584a);
    border: 3px solid var(--white);
  }
  .back-photo-2 {
    left: 263px; top: 237px; width: 138px; height: 138px;
    background: radial-gradient(circle at 50% 40%, #5c6a62, var(--board));
  }
  .banner {
    left: 55px; top: 387px; width: 408px; height: 28px; border-radius: 14px;
    background: var(--red); color: var(--white);
    font-size: 16px; font-weight: 600;
    display: flex; align-items: center; justify-content: center;
  }
  .service {
    top: 438px; height: 152px; border-radius: 8px; border: 2.5px solid;
    text-align: center; padding: 9px 6px 0;
  }
  .service h3 { font-size: 13.5px; font-weight: 500; line-height: 1.2; margin-bottom: 9px; white-space: nowrap; }
  .service p { font-size: 9.2px; line-height: 1.25; }
  .service-test { left: 26px; width: 150px; background: var(--white); border-color: var(--red); color: var(--navy); }
  .service-test h3 { color: var(--red); }
  .service-thinking { left: 183px; width: 150px; background: var(--yellow); border-color: var(--white); color: var(--navy); }
  .service-thinking h3 { color: var(--white); }
  .service-advanced { left: 339px; width: 155px; background: var(--yellow); border-color: var(--navy); color: var(--navy); padding-top: 3px; }
  .service-advanced h3 { font-size: 13px; margin-bottom: 7px; }
  .back-contact {
    left: 0; width: 100%; top: 616px; display: flex; justify-content: center; align-items: center; gap: 9px;
    color: var(--navy); font-size: 16px; font-weight: 600;
  }
  .back-contact .phone-pill { background: var(--navy); margin-top: 0; font-weight: 600; }
</style>
</head>
<body>

<section class="flyer flyer-front" aria-label="Flyer front">
  <svg class="shapes" viewBox="0 0 520 672" aria-hidden="true">
    <circle cx="150" cy="100" r="250" fill="var(--yellow)"/>
    <polygon points="520,190 520,672 180,672" fill="var(--navy)"/>
  </svg>

  <h1 class="abs headline">BACK<br>TO<br>SCHOOL</h1>
  <div class="abs headline-rule"></div>
  <h2 class="abs subhead">Support Online<br>Learning</h2>

  <div class="abs brand"><span class="brand-dot"></span>QN Academy</div>

  <div class="abs photo front-photo" role="img" aria-label="Photo of a young girl in glasses reading a book in front of a bookshelf"></div>

  <h2 class="abs section-title">About Us</h2>
  <div class="abs about-text">
    <p>QN Academy in Maple Ridge/Cedar Falls, Georgia is a private tutoring center which provides group coaching in Math, Reading, KEV Preparation, and Computer Programming for kids.</p>
    <p>We also provide effective coaching for standardized tests like KEV, IRPA, NUR, etc. We step away from the regular coaching method and implement effective problem solving techniques and critical thinking skills to help our children achieve stronger academic results.</p>
  </div>

  <div class="abs test-tags">
    <span class="tag tag-navy">KEVs</span>
    <span class="tag tag-red">NURs</span>
  </div>
  <div class="abs tags-caption">EFFECTIVE TEST PREPARATION</div>

  <div class="abs front-contact">
    <div class="contact-label">Contact Us</div>
    <span class="phone-pill">555-014-2236</span>
  </div>
</section>

<section class="flyer flyer-back" aria-label="Flyer back">
  <svg class="shapes" viewBox="0 0 517 670" aria-hidden="true">
    <ellipse cx="420" cy="650" rx="420" ry="330" fill="var(--yellow)"/>
    <ellipse cx="200" cy="160" rx="300" ry="215" fill="var(--navy)"/>
  </svg>

  <h2 class="abs back-title">Our Academy</h2>
  <div class="abs back-text">
    <p class="p-wide">Our Georgia Standard Education (GSE) Subjects Tutoring Programs are designed to reinforce and enhance the material that our children are learning in school only a few hours before. By focusing on a topic with our skilled teachers after school, students are guaranteed to have a strong foundation and understanding of their topics before moving on to learning more advanced skills.</p>
    <p class="p-mid">With our online learning course we have created a platform with live instructor interaction, virtual classroom, instructional videos, assessments, and practice to support every individual student's need. We are confident in our ability to provide the most effective distance learning experience.</p>
    <p class="p-narrow">QN Academy strives to improve your children's academic achievements and analytical problem solving skills. We believe that stretching a child's mind through critical thinking skills, accelerated academic programs, and exposure to computer programming and robotics at an early age will help them rise to their true potential.</p>
  </div>

  <div class="abs photo back-photo-1" role="img" aria-label="Photo of a teacher helping a girl with her schoolwork"></div>
  <div class="abs photo back-photo-2" role="img" aria-label="Photo of a boy with an idea in front of a chalkboard"></div>

  <div class="abs banner">A Place to Enrich Students' Potentials</div>

  <article class="abs service service-test">
    <h3>Test Preparation</h3>
    <p>We provide specialized and effective test preparation courses in KEV. "Practice Makes Perfect". We get students into a routine of consistent practice of various concepts required for success on the KEV test.</p>
  </article>
  <article class="abs service service-thinking">
    <h3>Critical Thinking</h3>
    <p>We provide excellent critical and analytical thinking practice. Our program also helps students develop valuable tools to properly prepare for standardized tests like FMAT, IRPA, etc.</p>
  </article>
  <article class="abs service service-advanced">
    <h3>Advanced<br>Academic Coaching</h3>
    <p>We offer advanced coaching in all academic subjects for grade 1 to grade 12. Our Mathematics and Language Arts courses follow common core standards.</p>
  </article>

  <div class="abs back-contact">
    <span>Contact Us</span>
    <span class="phone-pill">555-014-2236</span>
  </div>
</section>

</body>
</html>
```